Velliora Events Business Card

We need a business cards that stands out to our clients. We are company who targets prestige clients to spend money with us on experiences, so our image needs to be prestige
Target Market(s)
Corporate
Contact Information for Business Card
There will be four different names on the business cards
Danielle Brontoss
Director
O: 02 5174 2038
M: 0491 652 083
E: info@vellioraevents.example.com.au
Facebook: @vellioraevents
Instagram: vellioraevents
www.vellioraevents.example.com.au
Nathaniel Brontoss
Director
O: 02 5174 2038
M: 0478 205 946
Facebook: @vellioraevents
Instagram: vellioraevents
www.vellioraevents.example.com.au
Elias Dorvek
Director
O: 02 5174 2038
M: 0467 319 752
Facebook: @vellioraevents
Instagram: vellioraevents
www.vellioraevents.example.com.au
Marta Quell
Director
O: 02 5174 2038
Facebook: @vellioraevents
Instagram: vellioraevents
www.vellioraevents.example.com.au
Colors
Designer to choose colors to be used in the design.
Look and feel

```html
<!DOCTYPE html>
<html lang="en">
<head>
<meta charset="utf-8">
<title>Velliora Events Business Card</title>
<link href="https://fonts.googleapis.com/css2?family=Roboto:wght@300;400;500;700&display=swap" rel="stylesheet">
<style>
  :root {
    --bg: #1c1c1e;
    --gold: #d3a94a;
    --gold-light: #f1dfa4;
    --gold-deep: #c79a38;
    --navy: #2a2462;
    --navy-light: #38306f;
    --white: #ffffff;
    --text-soft: #eceaf4;
  }
  html, body {
    margin: 0;
    width: 1200px;
    height: 960px;
    overflow: hidden;
    background: var(--bg);
    font-family: "Roboto", Arial, sans-serif;
  }
  .stage {
    width: 1200px;
    height: 960px;
    display: flex;
    flex-direction: column;
    align-items: center;
    justify-content: center;
    gap: 60px;
  }
  .card {
    position: relative;
    width: 700px;
    height: 400px;
    overflow: hidden;
    box-shadow: 0 14px 30px rgba(0,0,0,0.55);
  }
  /* Front */
  .card-front {
    background: radial-gradient(ellipse at 50% 35%, var(--gold-light) 0%, #e2c26f 40%, var(--gold-deep) 100%);
  }
  .front-brand {
    position: absolute;
    top: 150px;
    left: 0;
    right: 0;
    text-align: center;
    color: var(--white);
    font-weight: 300;
    font-size: 34px;
    letter-spacing: 10px;
    text-transform: uppercase;
  }
  .front-url {
    position: absolute;
    bottom: 60px;
    left: 0;
    right: 0;
    text-align: center;
    color: var(--white);
    font-weight: 400;
    font-size: 15px;
    letter-spacing: 6px;
  }
  /* Back */
  .card-back {
    background: linear-gradient(120deg, var(--navy) 0%, var(--navy) 55%, var(--navy-light) 100%);
  }
  .back-brand {
    position: absolute;
    top: 110px;
    left: 0;
    right: 0;
    text-align: center;
    color: var(--gold);
    font-weight: 300;
    font-size: 32px;
    letter-spacing: 10px;
    text-transform: uppercase;
  }
  .divider-bold {
    position: absolute;
    top: 232px;
    left: 40px;
    width: 260px;
    height: 4px;
    background: var(--white);
  }
  .divider-thin {
    position: absolute;
    top: 233px;
    left: 300px;
    width: 370px;
    height: 1px;
    background: var(--gold);
  }
  .person {
    position: absolute;
    top: 252px;
    left: 40px;
  }
  .person-name {
    margin: 0;
    color: var(--gold);
    font-weight: 700;
    font-size: 26px;
    text-transform: uppercase;
    line-height: 1.1;
  }
  .person-role {
    margin: 4px 0 6px;
    color: var(--white);
    font-weight: 500;
    font-size: 17px;
    text-transform: uppercase;
  }
  .person-address {
    margin: 0;
    color: var(--text-soft);
    font-weight: 400;
    font-size: 16px;
    line-height: 1.35;
  }
  .contacts {
    position: absolute;
    top: 250px;
    right: 30px;
    margin: 0;
    padding: 0;
    list-style: none;
  }
  .contact-item {
    display: flex;
    justify-content: flex-end;
    align-items: center;
    gap: 8px;
    color: var(--white);
    font-size: 15px;
    line-height: 22px;
  }
  .contact-icon {
    width: 13px;
    height: 13px;
    flex: none;
  }
</style>
</head>
<body>
<main class="stage">
  <section class="card card-front" aria-label="Card front">
    <div class="front-brand">Velliora Events</div>
    <div class="front-url">www.vellioraevents.example.com</div>
  </section>

  <section class="card card-back" aria-label="Card back">
    <div class="back-brand">Velliora Events</div>
    <div class="divider-bold"></div>
    <div class="divider-thin"></div>

    <div class="person">
      <h1 class="person-name">Owen Tarrick</h1>
      <p class="person-role">CEO/Founder</p>
      <p class="person-address">4120 Larkspur Row<br>Fenwick, Ardale 20871</p>
    </div>

    <ul class="contacts">
      <li class="contact-item">02 5174 2038
        <svg class="contact-icon" viewBox="0 0 16 16" aria-hidden="true"><path fill="#d3a94a" d="M3.5 1l2.5 3-1.5 1.8c.8 1.8 2.3 3.4 4.2 4.2L10.5 8.5l3 2.5-1.5 3C6.5 13.5 2.5 9.5 2 4z"/></svg>
      </li>
      <li class="contact-item">0491 652 083
        <svg class="contact-icon" viewBox="0 0 16 16" aria-hidden="true"><rect x="4" y="1" width="8" height="14" rx="1.5" fill="none" stroke="#d3a94a" stroke-width="1.6"/><circle cx="8" cy="12.5" r="0.9" fill="#d3a94a"/></svg>
      </li>
      <li class="contact-item">owen@vellioraevents.example.com
        <svg class="contact-icon" viewBox="0 0 16 16" aria-hidden="true"><rect x="1" y="3" width="14" height="10" fill="#d3a94a"/><path d="M1 3l7 6 7-6" fill="none" stroke="#2a2462" stroke-width="1.3"/></svg>
      </li>
      <li class="contact-item">www.vellioraevents.example.com
        <svg class="contact-icon" viewBox="0 0 16 16" aria-hidden="true"><circle cx="8" cy="8" r="7" fill="#d3a94a"/><ellipse cx="8" cy="8" rx="3" ry="7" fill="none" stroke="#2a2462" stroke-width="1"/><path d="M1 8h14" stroke="#2a2462" stroke-width="1"/></svg>
      </li>
    </ul>
  </section>
</main>
</body>
</html>
```